Battle of the Bands Flyer

We are looking to have a flyer made for Battle of the Bands event featuring kids. It is a fundraising event hosted by us, BELVIK Contracting. Proceeds raised from the event will benefit Maple and Harbor and Tillman School for Arts. This information should be reflected on the flyer somewhere, and will provide the logos.
We will post a sample of something we mocked up in AI for inspiration.
The title should be "Battle of the Bands".
The subtitle should be "Sky's the Limit"
The date of the event is February 27, 2025 at 5 pm.
The location of the event is Corvin Flight Museum in Irvine, CA.
To register for the event, you can put the contact email as jwelty@belvikcontracting.example.

```html
<!DOCTYPE html>
<html lang="en">
<head>
<meta charset="utf-8">
<title>Battle of the Bands – Sky's the Limit</title>
<link rel="stylesheet" href="https://fonts.googleapis.com/css2?family=Bebas+Neue&family=Montserrat:wght@400;500;700;800&family=Orbitron:wght@800&display=swap">
<style>
  :root {
    --page-bg: #ececec;
    --navy-top: #2c2d50;
    --navy-bottom: #0a0b2e;
    --flag-blue: #2d5a8e;
    --flag-red: #e23a52;
    --flag-white: #efefef;
    --text-light: #ffffff;
    --accent-red: #e8405a;
    --glow: #6c72a8;
    --badge-one: #c9c9cf;
    --badge-two: #f08a2c;
  }
  * { margin: 0; padding: 0; box-sizing: border-box; }
  html, body {
    width: 1200px; height: 1200px; overflow: hidden;
    background: var(--page-bg);
  }
  .flyer {
    position: absolute;
    left: 205px; top: 41px;
    width: 790px; height: 1118px;
  }
  .flyer svg { display: block; width: 100%; height: 100%; }
  .headline { font-family: "Bebas Neue", "Anton", sans-serif; fill: var(--text-light); }
  .tagline { font-family: "Orbitron", sans-serif; font-weight: 800; fill: var(--text-light); }
  .info { font-family: "Montserrat", sans-serif; fill: var(--text-light); }
  .info-bold { font-weight: 800; }
  .info-medium { font-weight: 500; }
  .info-regular { font-weight: 400; }
  .time { fill: var(--accent-red); }
  .year { fill: var(--navy-bottom); }
  .host-name { font-family: "Montserrat", sans-serif; font-weight: 700; fill: var(--text-light); }
</style>
</head>
<body>
<main class="flyer">
  <svg viewBox="0 0 972 1376" xmlns="http://www.w3.org/2000/svg" aria-labelledby="flyer-title">
    <title id="flyer-title">Battle of the Bands – Sky's the Limit, 27 February 2025</title>
    <defs>
      <linearGradient id="bg-navy" x1="0" y1="0" x2="0" y2="1">
        <stop offset="0" stop-color="var(--navy-top)"/>
        <stop offset="1" stop-color="var(--navy-bottom)"/>
      </linearGradient>
      <radialGradient id="stage-glow" cx="0.5" cy="0.35" r="0.6">
        <stop offset="0" stop-color="var(--glow)" stop-opacity="0.75"/>
        <stop offset="0.6" stop-color="var(--glow)" stop-opacity="0.2"/>
        <stop offset="1" stop-color="var(--glow)" stop-opacity="0"/>
      </radialGradient>
      <pattern id="flag-stripes" width="60" height="48" patternUnits="userSpaceOnUse" patternTransform="rotate(21.8)">
        <rect width="60" height="24" fill="var(--flag-red)"/>
        <rect y="24" width="60" height="24" fill="var(--flag-white)"/>
      </pattern>
    </defs>

    <!-- Background -->
    <rect class="flyer-bg" width="972" height="1376" fill="url(#bg-navy)"/>

    <!-- Stage photo area -->
    <rect class="stage-photo" x="0" y="560" width="972" height="530" fill="url(#stage-glow)"
          role="img" aria-label="Photo of a children's band performing on stage in silhouette under spotlights"/>

    <!-- Flag corner -->
    <polygon class="flag-stripes" points="470,0 972,0 972,305 465,100" fill="url(#flag-stripes)"/>
    <polygon class="flag-field" points="0,0 505,0 522,88 0,339" fill="var(--flag-blue)"/>

    <!-- Host -->
    <text class="host-name" x="486" y="232" text-anchor="middle" font-size="34" textLength="300" lengthAdjust="spacingAndGlyphs">BELVIK CONTRACTING</text>

    <!-- Title -->
    <text class="headline" x="250" y="457" font-size="205" textLength="378" lengthAdjust="spacingAndGlyphs">BATTLE</text>
    <text class="headline" x="660" y="380" font-size="64" textLength="70" lengthAdjust="spacingAndGlyphs">OF</text>
    <text class="headline" x="660" y="430" font-size="64" textLength="70" lengthAdjust="spacingAndGlyphs">THE</text>
    <text class="headline" x="200" y="712" font-size="330" textLength="570" lengthAdjust="spacingAndGlyphs">BANDS</text>

    <text class="tagline" x="200" y="779" font-size="50" textLength="572" lengthAdjust="spacingAndGlyphs">SKY'S THE LIMIT</text>

    <!-- Date -->
    <text class="info info-bold" x="205" y="1155" font-size="66" textLength="88" lengthAdjust="spacingAndGlyphs">27</text>
    <text class="info info-bold" x="205" y="1197" font-size="48" textLength="88" lengthAdjust="spacingAndGlyphs">FEB</text>
    <rect class="year-box" x="205" y="1201" width="88" height="27" fill="var(--text-light)"/>
    <text class="info info-bold year" x="210" y="1224" font-size="25" textLength="78" lengthAdjust="spacingAndGlyphs">2025</text>

    <rect class="divider" x="330" y="1097" width="4" height="145" fill="var(--text-light)"/>

    <!-- Venue -->
    <text class="info info-bold" x="372" y="1137" font-size="38" textLength="396" lengthAdjust="spacingAndGlyphs">CORVIN FLIGHT MUSEUM IN</text>
    <text class="info info-bold" x="372" y="1171" font-size="38" textLength="208" lengthAdjust="spacingAndGlyphs">IRVINE, CA.</text>
    <text class="info info-bold time" x="600" y="1171" font-size="38" textLength="170" lengthAdjust="spacingAndGlyphs">05:00 PM</text>

    <text class="info info-bold" x="380" y="1205" font-size="17" textLength="382" lengthAdjust="spacingAndGlyphs">SEND AN EMAIL TO REGISTER FOR THE EVENT</text>
    <text class="info info-regular" x="571" y="1232" text-anchor="middle" font-size="21" textLength="340" lengthAdjust="spacingAndGlyphs">jwelty@belvikcontracting.example</text>

    <!-- Beneficiaries band -->
    <rect class="beneficiary-band" x="0" y="1252" width="972" height="124" fill="var(--flag-blue)"/>
    <text class="info info-medium" x="100" y="1312" font-size="17" textLength="477" lengthAdjust="spacingAndGlyphs">PROCEEDS RAISED FROM THE EVENT WILL BENEFIT</text>
    <text class="info info-medium" x="100" y="1335" font-size="17" textLength="477" lengthAdjust="spacingAndGlyphs">MAPLE AND HARBOR AND TILLMAN SCHOOL FOR ARTS</text>

    <circle class="partner-badge" cx="684" cy="1312" r="30" fill="var(--badge-one)"/>
    <rect class="partner-badge" x="790" y="1284" width="56" height="56" fill="var(--badge-two)"/>
  </svg>
</main>
</body>
</html>
```